Brennick Holdings Business Cards

These are professional business cards that are for my family office.
Put fake emails and phone numbers as of now until I finalize those components. This family office controls my families investments, assets, and future. The cards should be professional.
..
.
.
.
I just uploaded another variation of a logo I would like to see as a business card to I am inbeteen which logo to use

Target Market(s)

business

Industry/Entity Type

business

Contact Information for Business Card

Professional, wealth related, finance related.

Requirements
Must have
• Logo

```html
<!DOCTYPE html>
<html lang="en">
<head>
<meta charset="utf-8">
<title>Brennick Holdings — Business Cards</title>
<link rel="stylesheet" href="https://fonts.googleapis.com/css2?family=Cinzel:wght@500&family=Montserrat:wght@400;500;600;700&display=swap">
<style>
  :root {
    --ink: #2c2e39;
    --stone: #b0afab;
    --paper: #ffffff;
    --backdrop: #ececec;
  }
  * { margin: 0; padding: 0; box-sizing: border-box; }
  html, body {
    width: 1200px;
    height: 1200px;
    overflow: hidden;
    background: var(--backdrop);
  }
  .card {
    position: absolute;
    left: 181px;
    width: 845px;
    height: 482px;
  }
  .card-front {
    top: 94px;
    background: var(--ink);
    color: var(--paper);
  }
  .card-back {
    top: 631px;
    background: var(--paper);
    color: var(--ink);
  }
  .brand-name {
    font-family: "Cinzel", serif;
    font-weight: 500;
    white-space: nowrap;
    position: absolute;
    left: 0;
    width: 100%;
    text-align: center;
  }
  .front-ring {
    position: absolute;
    left: 344px;
    top: 137px;
    width: 160px;
    height: 160px;
  }
  .card-front .brand-name {
    top: 318px;
    font-size: 33px;
    letter-spacing: 1px;
  }
  .front-website {
    position: absolute;
    right: 51px;
    top: 427px;
    font-family: "Montserrat", sans-serif;
    font-size: 18px;
    letter-spacing: 0.3px;
  }
  .card-back .brand-name {
    top: 76px;
    font-size: 45px;
    letter-spacing: 1px;
  }
  .side-tab {
    position: absolute;
    left: 0;
    top: 204px;
    width: 15px;
    height: 74px;
    background: var(--stone);
  }
  .holder-name {
    position: absolute;
    left: 75px;
    top: 206px;
    font-family: "Montserrat", sans-serif;
    font-weight: 700;
    font-size: 33px;
    letter-spacing: 4px;
  }
  .holder-title {
    position: absolute;
    left: 75px;
    top: 247px;
    font-family: "Montserrat", sans-serif;
    font-weight: 700;
    font-size: 19px;
  }
  .divider {
    position: absolute;
    left: 75px;
    top: 293px;
    width: 696px;
    height: 2px;
    background: var(--ink);
  }
  .contact-list {
    list-style: none;
    position: absolute;
    left: 75px;
    top: 317px;
    font-family: "Montserrat", sans-serif;
    font-size: 17px;
  }
  .contact-list li {
    display: flex;
    align-items: center;
    height: 25px;
    margin-bottom: 8px;
  }
  .contact-icon {
    width: 25px;
    height: 25px;
    margin-right: 16px;
    flex: none;
  }
  .contact-phone { letter-spacing: 2.5px; }
  .address {
    position: absolute;
    right: 75px;
    top: 383px;
    font-family: "Montserrat", sans-serif;
    font-size: 17px;
  }
</style>
</head>
<body>

<section class="card card-front">
  <svg class="front-ring" viewBox="0 0 160 160" aria-hidden="true">
    <circle cx="80" cy="80" r="78" fill="none" stroke="#ffffff" stroke-width="3"/>
  </svg>
  <h1 class="brand-name">Brennick Holdings</h1>
  <p class="front-website">www.yourwebsite.com</p>
</section>

<section class="card card-back">
  <h2 class="brand-name">Brennick Holdings</h2>
  <div class="side-tab"></div>
  <p class="holder-name">Your Name</p>
  <p class="holder-title">Your Title</p>
  <div class="divider"></div>
  <ul class="contact-list">
    <li>
      <svg class="contact-icon" viewBox="0 0 25 25" aria-hidden="true">
        <circle cx="12.5" cy="12.5" r="12.5" fill="var(--stone)"/>
        <path d="M8 6.5l2.5-.5 1.4 3.2-1.6 1.2c.8 1.7 2 2.9 3.7 3.7l1.2-1.6 3.2 1.4-.5 2.5c-.2.6-.7 1-1.4 1C10.9 17.2 7.8 14.1 7 9.4c0-.7.4-1.3 1-1.6z" fill="#ffffff"/>
      </svg>
      <span class="contact-phone">123-456-789</span>
    </li>
    <li>
      <svg class="contact-icon" viewBox="0 0 25 25" aria-hidden="true">
        <circle cx="12.5" cy="12.5" r="12.5" fill="var(--stone)"/>
        <g fill="none" stroke="#ffffff" stroke-width="1.1">
          <circle cx="12.5" cy="12.5" r="6.5"/>
          <ellipse cx="12.5" cy="12.5" rx="3" ry="6.5"/>
          <line x1="6" y1="12.5" x2="19" y2="12.5"/>
          <line x1="7" y1="9.2" x2="18" y2="9.2"/>
          <line x1="7" y1="15.8" x2="18" y2="15.8"/>
        </g>
      </svg>
      <span>www.yourwebsite.com</span>
    </li>
    <li>
      <svg class="contact-icon" viewBox="0 0 25 25" aria-hidden="true">
        <circle cx="12.5" cy="12.5" r="12.5" fill="var(--stone)"/>
        <g fill="none" stroke="#ffffff" stroke-width="1.1">
          <rect x="6.5" y="8.5" width="12" height="8"/>
          <polyline points="6.5,8.5 12.5,13 18.5,8.5"/>
        </g>
      </svg>
      <span>email@info.com</span>
    </li>
  </ul>
  <p class="address">Your Address and Country</p>
</section>

</body>
</html>
```